Excavator Wrap/Car wrap similar

Hi

I already have my car wrap desgin and want to bring it over to the excavtor

I would like it to look similar but with more graphics

Dont be boring or plan i want this to stand out

Use the colours as shown with my car wraps

It is a plumbing company as you can see

I have attached photos of excavtor sides and rear

Target Market(s)

Plumbing industry

Industry/Entity Type

Plumber

Requirements
Must have
• Must have my logo
Use the colours on my truck
Contact numbers
Nice to have
• Look at other excavators and get ideas from them
Should not have
• boring
Plain

```html
<!DOCTYPE html>
<html lang="en">
<head>
<meta charset="utf-8">
<title>Cleared Plumbing Services – Excavator Wrap Panels</title>
<link href="https://fonts.googleapis.com/css2?family=Anton&family=Exo+2:wght@800&display=swap" rel="stylesheet">
<style>
  :root {
    --stage: #878787;
    --divider: #1c1c1c;
    --wrap-blue: #1f6bff;
    --wrap-blue-deep: #0a4fe6;
    --wrap-blue-light: #5c9dff;
    --sky-light: #a9d3ff;
    --sky-pale: #e6f4ff;
    --brand-cyan: #00a6e8;
    --brand-navy: #0b5aa8;
    --window-grey: #bdbdbd;
    --cut-line: #e0141b;
    --white: #ffffff;
    --label-ink: #000000;
  }
  html, body {
    margin: 0;
    padding: 0;
    overflow: hidden;
    background: var(--stage);
  }
  .wrap-sheet {
    display: block;
    width: 1200px;
    height: 1000px;
  }
  .panel-label {
    font-family: "Anton", "Oswald", sans-serif;
    font-size: 40px;
    fill: var(--label-ink);
    text-anchor: middle;
  }
  .phone-number {
    font-family: "Anton", sans-serif;
    fill: var(--white);
  }
  .service-hours {
    font-family: "Anton", sans-serif;
  }
  .service-hours--light { fill: var(--white); }
  .service-hours--dark { fill: var(--brand-navy); }
  .boom-slogan {
    font-family: "Anton", sans-serif;
    font-size: 68px;
    fill: var(--white);
  }
  .brand-name {
    font-family: "Exo 2", sans-serif;
    font-weight: 800;
    font-size: 62px;
    fill: var(--brand-cyan);
  }
  .brand-tagline {
    font-family: "Exo 2", sans-serif;
    font-weight: 800;
    font-size: 19px;
    fill: var(--brand-navy);
  }
  .cut-line {
    fill: none;
    stroke: var(--cut-line);
    stroke-width: 2;
  }
  .window { fill: var(--window-grey); }
  .divider { stroke: var(--divider); stroke-width: 2; }
</style>
</head>
<body>
<svg class="wrap-sheet" viewBox="0 0 2100 1750" xmlns="http://www.w3.org/2000/svg">
  <defs>
    <linearGradient id="deep-blue" x1="0" y1="0" x2="1" y2="1">
      <stop offset="0" stop-color="#0a4fe6"/>
      <stop offset="0.55" stop-color="#2a78ff"/>
      <stop offset="1" stop-color="#1f63f2"/>
    </linearGradient>
    <linearGradient id="band-blue" x1="0" y1="0" x2="0" y2="1">
      <stop offset="0" stop-color="#5c9dff"/>
      <stop offset="1" stop-color="#0f5af5"/>
    </linearGradient>
    <linearGradient id="back-water" x1="0" y1="0" x2="0" y2="1">
      <stop offset="0" stop-color="#ffffff"/>
      <stop offset="0.5" stop-color="#ffffff"/>
      <stop offset="0.68" stop-color="#cfe6fb"/>
      <stop offset="1" stop-color="#5fa6f5"/>
    </linearGradient>
    <linearGradient id="sky-water" x1="0" y1="0" x2="0" y2="1">
      <stop offset="0" stop-color="#7cb6fb"/>
      <stop offset="0.55" stop-color="#cfe8fd"/>
      <stop offset="1" stop-color="#8ec7f7"/>
    </linearGradient>
    <linearGradient id="boom-blue" x1="0" y1="0" x2="1" y2="1">
      <stop offset="0" stop-color="#1c66ff"/>
      <stop offset="1" stop-color="#3a86ff"/>
    </linearGradient>
  </defs>

  <rect width="2100" height="1750" fill="var(--stage)"/>
  <line class="divider" x1="1154" y1="0" x2="1154" y2="1750"/>
  <line class="divider" x1="0" y1="933" x2="2100" y2="933"/>

  <!-- Right side -->
  <g class="panel panel-right">
    <path role="img" aria-label="Cab panel with blue water wave and bubble backdrop"
      d="M615,195 L665,190 L680,210 L960,95 Q1000,82 1035,85 Q1070,95 1082,150 L1105,372 L990,388 Q950,402 932,450 L918,520 L668,520 L668,415 L615,415 Z"
      fill="url(#deep-blue)"/>
    <path class="cut-line" d="M626,207 L663,203 L678,215 L962,108 L1030,97 Q1062,108 1070,160 L1093,362 L988,377 Q945,395 925,450 L912,508 L680,508 L680,408 L626,408 Z"/>
    <path class="window" d="M768,305 L965,215 Q1000,208 995,235 L968,315 Q955,335 930,345 L762,370 Z"/>
    <path class="window" d="M750,405 L930,365 Q938,367 934,378 L900,470 Q893,478 880,478 L748,478 Q744,440 750,405 Z"/>

    <path role="img" aria-label="Lower panel with blue water and bubble backdrop"
      d="M122,528 L925,525 L880,785 L185,785 Q122,775 118,700 Z" fill="url(#band-blue)"/>
    <path class="cut-line" d="M130,537 L912,537 L870,772 L190,772 Q132,765 130,700 Z"/>

    <g class="service-hours service-hours--light">
      <text x="160" y="646" font-size="80">24/7</text>
      <text x="166" y="678" font-size="30">service</text>
    </g>
    <circle class="window" cx="584" cy="581" r="15"/>
    <rect class="window" x="725" y="582" width="141" height="25" rx="12"/>
    <rect class="window" x="370" y="627" width="482" height="37" rx="18"/>
    <path d="M172,706 q-10,8 -5,22 q12,24 36,32 q12,3 18,-6 l-2,-6 l-16,-7 l-7,6 q-12,-6 -18,-19 l6,-7 l-6,-16 l-6,1 z" fill="var(--white)"/>
    <text class="phone-number" x="234" y="752" font-size="66" textLength="632" lengthAdjust="spacingAndGlyphs">5550 2186 - 0400 555 424</text>
    <text class="panel-label" x="596" y="846">Right side</text>
  </g>

  <!-- Back side -->
  <g class="panel panel-back">
    <path role="img" aria-label="Rear panel, white top fading into a blue water wave and bubble backdrop"
      d="M1370,378 Q1385,360 1480,368 L1950,372 Q1978,360 1982,385 L2002,600 Q2005,680 1962,712 L1720,770 Q1600,792 1400,748 Q1350,722 1346,640 L1362,430 Z"
      fill="url(#back-water)"/>
    <path d="M1370,378 Q1385,360 1480,368 L1485,376 Q1420,395 1368,425 Z" fill="var(--wrap-blue)"/>
    <path class="cut-line" d="M1392,385 L1950,397 Q1958,400 1957,410 L1980,640 L1952,718 L1720,762 L1380,720 L1366,640 Z"/>
    <circle cx="1503" cy="518" r="108" fill="var(--brand-navy)"/>
    <text class="brand-name" x="1632" y="472" textLength="248" lengthAdjust="spacingAndGlyphs">CLEARED</text>
    <text class="brand-name" x="1632" y="528" textLength="288" lengthAdjust="spacingAndGlyphs">PLUMBING</text>
    <text class="brand-name" x="1632" y="584" textLength="263" lengthAdjust="spacingAndGlyphs">SERVICES</text>
    <text class="brand-tagline" x="1634" y="606" textLength="258" lengthAdjust="spacingAndGlyphs">YOUR LOCAL, TRUSTED PLUMBER</text>
    <text class="panel-label" x="1712" y="846">back side</text>
  </g>

  <!-- Boom: both sides -->
  <g class="panel panel-boom">
    <path role="img" aria-label="Boom strip with blue water and bubble backdrop"
      d="M82,1045 L230,1015 Q300,995 440,1000 Q620,1020 780,1180 L1090,1515 Q1105,1545 1090,1572 L1062,1618 Q1040,1635 1018,1614 L720,1340 Q520,1172 320,1138 L90,1132 Z"
      fill="url(#boom-blue)"/>
    <path class="cut-line" d="M102,1055 L235,1030 Q300,1015 440,1020 Q610,1040 765,1195 L1072,1545 L1048,1600 L735,1325 Q525,1155 310,1120 L105,1112 Z"/>
    <text class="boom-slogan" transform="translate(272,1092) rotate(17)">Your local</text>
    <text class="boom-slogan" transform="translate(600,1182) rotate(40)">trusted plumber</text>
    <circle cx="1022" cy="1545" r="55" fill="var(--white)"/>
    <text class="panel-label" x="641" y="1683">Both left and right side</text>
  </g>

  <!-- Left side -->
  <g class="panel panel-left">
    <path role="img" aria-label="Cab panel with light sky-blue water wave and bubble backdrop"
      d="M1290,1080 Q1310,1028 1390,1025 L1740,1028 Q1772,1035 1776,1075 L1870,1115 Q1935,1160 1940,1260 L1945,1350 Q1935,1385 1900,1385 L1410,1385 Q1385,1380 1380,1340 L1365,1282 L1252,1278 Q1238,1268 1245,1240 Z"
      fill="url(#sky-water)"/>
    <path class="cut-line" d="M1285,1105 Q1300,1045 1390,1038 L1745,1045 L1765,1080 L1862,1125 Q1918,1170 1925,1265 L1930,1360 L1398,1362 L1392,1300 L1370,1270 L1265,1250 Z"/>
    <path class="window" d="M1355,1165 L1520,1210 L1555,1255 L1395,1258 Z"/>
    <path class="window" d="M1400,1262 L1550,1285 L1575,1330 L1420,1335 Z"/>
    <g class="service-hours service-hours--dark">
      <text x="1596" y="1262" font-size="140">24/7</text>
      <text x="1606" y="1304" font-size="46">service</text>
    </g>

    <path role="img" aria-label="Lower panel with blue water and bubble backdrop"
      d="M1400,1397 L2000,1385 Q2030,1390 2026,1430 L2020,1540 Q2010,1606 1930,1610 L1445,1613 Q1425,1606 1420,1560 Z"
      fill="url(#band-blue)"/>
    <path class="cut-line" d="M1420,1418 L2003,1405 Q2010,1410 2006,1430 L1998,1545 Q1985,1584 1930,1588 L1452,1592 Z"/>
    <rect class="window" x="1474" y="1473" width="367" height="34" rx="17"/>
    <path d="M1485,1533 q-8,6 -4,17 q9,18 27,24 q9,2 14,-5 l-2,-5 l-12,-5 l-5,5 q-9,-5 -14,-14 l5,-5 l-5,-12 l-4,1 z" fill="var(--white)"/>
    <text class="phone-number" x="1535" y="1565" font-size="46" textLength="415" lengthAdjust="spacingAndGlyphs">5550 2186 - 0400 555 424</text>
    <text class="panel-label" x="1705" y="1683">Left side</text>
  </g>
</svg>
</body>
</html>
```